Business Card Design - Property Management & Real Estate Services

I need a business card design for my company that I can print ZEP Cards. The company is called Brisk Management Company. It is a property management and real estate company. The design has to be clean and modern. I need two versions. One for my employee and one for me. However, the design will be the same, just different text. You can get a feel for the company by looking at our website at www.briskmanagement.example.

Industry/Entity Type

Property Management

Contact Information for Business Card

I will be using ZEP.com to print my cards. I will most likely use the rounded edges card. I need two versions, however, they will be the same design. I need one for me and my employee.

Colors
3276b5
33a6d7

Requirements
Must have
• Company Logo
• Name of person
• Property Management & Real Estate Service
• Phone
• Email
• Website
• Address
• A space to place a QR code

```html
<!DOCTYPE html>
<html lang="en">
<head>
<meta charset="utf-8">
<title>Brisk Management Company – Business Card</title>
<link href="https://fonts.googleapis.com/css2?family=Roboto:wght@400;500;700&family=Exo+2:wght@700&display=swap" rel="stylesheet">
<style>
  :root {
    --bg: #b9b9b9;
    --card: #f7f7f5;
    --brand-dark: #1f4fa3;
    --brand-light: #5a8fd0;
    --ink: #3d3d3d;
    --rule: #7da6d8;
  }
  * { box-sizing: border-box; margin: 0; padding: 0; }
  html, body { width: 1200px; height: 852px; overflow: hidden; }
  body {
    background: var(--bg);
    font-family: "Roboto", Arial, sans-serif;
    color: var(--ink);
    position: relative;
  }
  .card {
    position: absolute;
    width: 500px;
    height: 286px;
    background: var(--card);
    border-radius: 14px;
    overflow: hidden;
    box-shadow: 0 6px 16px rgba(0,0,0,0.22);
  }
  .card--front { left: 70px; top: 283px; }
  .card--back { left: 630px; top: 283px; }

  /* Front */
  .front-brand {
    position: absolute;
    left: 0; right: 0; top: 88px;
    text-align: center;
  }
  .wordmark {
    display: inline-flex;
    align-items: center;
    gap: 10px;
    font-weight: 500;
    color: var(--brand-dark);
    letter-spacing: 0.06em;
  }
  .wordmark__mark {
    width: 14px; height: 14px;
    background: var(--brand-dark);
  }
  .front-brand .wordmark { font-size: 30px; }
  .front-brand .wordmark span { line-height: 1; }
  .front-web {
    position: absolute;
    left: 0; right: 0; top: 196px;
    display: flex; justify-content: center; align-items: center; gap: 14px;
    font-size: 13px;
  }
  .front-web::before, .front-web::after {
    content: ""; width: 34px; height: 1px; background: var(--brand-dark);
  }
  .edge-band {
    position: absolute; left: 0; right: 0; bottom: 0; height: 9px;
    display: flex;
  }
  .edge-band__light { flex: 0 0 42%; background: var(--brand-light); }
  .edge-band__dark { flex: 1; background: var(--brand-dark); }

  /* Back */
  .back-brand {
    position: absolute; left: 30px; top: 38px;
  }
  .back-brand .wordmark { font-size: 22px; }
  .back-rule-top {
    position: absolute; left: 30px; right: 30px; top: 76px;
    height: 1px; background: var(--rule);
  }
  .person {
    position: absolute; right: 30px; top: 28px; text-align: right;
  }
  .person__name {
    font-family: "Exo 2", "Roboto", sans-serif;
    font-weight: 700; font-size: 17px; color: var(--brand-dark);
  }
  .person__role { font-size: 12px; margin-top: 3px; }
  .address {
    position: absolute; right: 30px; top: 96px;
    text-align: right; font-size: 12.5px; line-height: 1.55;
  }
  .back-rule-bottom {
    position: absolute; left: 30px; right: 30px; top: 190px;
    height: 1px; background: var(--rule);
  }
  .contacts {
    position: absolute; left: 30px; top: 202px;
    list-style: none; font-size: 13px; line-height: 1.6;
  }
  .contacts li { display: flex; align-items: center; gap: 8px; }
  .contacts svg { width: 11px; height: 11px; fill: var(--brand-dark); flex: none; }
</style>
</head>
<body>

<section class="card card--front" aria-label="Card front">
  <div class="front-brand">
    <div class="wordmark"><i class="wordmark__mark"></i><span>BRISK MANAGEMENT</span></div>
  </div>
  <p class="front-web">www.briskmanagement.example</p>
  <div class="edge-band"><div class="edge-band__light"></div><div class="edge-band__dark"></div></div>
</section>

<section class="card card--back" aria-label="Card back">
  <div class="back-brand">
    <div class="wordmark"><i class="wordmark__mark"></i><span>BRISK MANAGEMENT</span></div>
  </div>
  <div class="person">
    <p class="person__name">Mateo R. Alvarez</p>
    <p class="person__role">Founder</p>
  </div>
  <div class="back-rule-top"></div>
  <address class="address" style="font-style:normal">
    480 Harbor Lane<br>#210 Coral Bay, FL 30000
  </address>
  <div class="back-rule-bottom"></div>
  <ul class="contacts">
    <li>
      <svg viewBox="0 0 24 24" aria-hidden="true"><path d="M6.6 10.8a15 15 0 0 0 6.6 6.6l2.2-2.2c.3-.3.7-.4 1-.2 1.1.4 2.3.6 3.6.6.6 0 1 .4 1 1V20c0 .6-.4 1-1 1A17 17 0 0 1 3 4c0-.6.4-1 1-1h3.5c.6 0 1 .4 1 1 0 1.3.2 2.5.6 3.6.1.3 0 .7-.2 1z"/></svg>
      (555) 010-4821
    </li>
    <li>
      <svg viewBox="0 0 24 24" aria-hidden="true"><path d="M2 5h20v14H2z M3 6l9 7 9-7" fill="none" stroke="#1f4fa3" stroke-width="2.5"/></svg>
      mateo@briskmanagement.example
    </li>
    <li>
      <svg viewBox="0 0 24 24" aria-hidden="true"><circle cx="12" cy="12" r="10"/><path d="M2 12h20M12 2c3 3 3 17 0 20M12 2c-3 3-3 17 0 20" fill="none" stroke="#f7f7f5" stroke-width="1.5"/></svg>
      www.briskmanagement.example
    </li>
  </ul>
</section>

</body>
</html>
```